Velmora Biz Card 2019

New business card for Velmora Property Inspections. We are a residential home inspection company in Arizona.

Target Market(s)

Real Estate

Font styles to use
Sans Serif

Requirements
Must have
• Glen Mirewick
• Home Inspector
• Velmora Property Inspections, LLC
• 480-555-0172
• glen@velmora-llc.example

```html
<!DOCTYPE html>
<html lang="en">
<head>
<meta charset="utf-8">
<title>Velmora Biz Card 2019</title>
<link rel="stylesheet" href="https://fonts.googleapis.com/css2?family=Open+Sans:wght@400;700;800&display=swap">
<style>
  :root {
    --backdrop: #e7e5e2;
    --card: #0e0e0e;
    --green: #3fb33f;
    --white: #f2f2f2;
  }
  * { box-sizing: border-box; margin: 0; padding: 0; }
  html, body {
    width: 1200px;
    height: 1200px;
    overflow: hidden;
    background: var(--backdrop);
    font-family: "Open Sans", Arial, sans-serif;
  }
  .canvas {
    width: 1200px;
    height: 1200px;
    display: flex;
    align-items: center;
    justify-content: center;
  }
  .business-card {
    position: relative;
    width: 1000px;
    height: 572px;
    background: var(--card);
    border-radius: 4px;
    box-shadow: 0 18px 40px rgba(0,0,0,0.25);
  }
  .brand {
    position: absolute;
    left: 70px;
    top: 250px;
    width: 380px;
    display: flex;
    align-items: center;
    justify-content: center;
    gap: 18px;
  }
  .brand-dot {
    width: 30px;
    height: 30px;
    border-radius: 50%;
    background: var(--green);
  }
  .brand-name {
    color: var(--white);
    font-weight: 800;
    font-size: 56px;
    letter-spacing: 3px;
    line-height: 1;
  }
  .divider {
    position: absolute;
    left: 475px;
    top: 200px;
    width: 2px;
    height: 180px;
    background: var(--green);
  }
  .contact {
    position: absolute;
    left: 515px;
    top: 190px;
    color: var(--white);
  }
  .contact-name {
    color: var(--green);
    font-weight: 800;
    font-size: 44px;
    line-height: 1.05;
  }
  .contact-title {
    font-size: 21px;
    margin-top: 4px;
  }
  .contact-company {
    color: var(--green);
    font-size: 21px;
    margin-top: 6px;
  }
  .contact-address {
    font-size: 21px;
    margin-top: 2px;
  }
  .contact-lines {
    list-style: none;
    margin-top: 10px;
  }
  .contact-lines li {
    display: flex;
    align-items: center;
    gap: 10px;
    font-size: 21px;
    line-height: 1.45;
  }
  .contact-icon {
    width: 16px;
    height: 16px;
    flex: none;
  }
</style>
</head>
<body>
  <main class="canvas">
    <section class="business-card">
      <div class="brand">
        <span class="brand-dot"></span>
        <span class="brand-name">VELMORA</span>
      </div>
      <div class="divider"></div>
      <div class="contact">
        <h1 class="contact-name">Glen Mirewick</h1>
        <p class="contact-title">Home Inspector</p>
        <p class="contact-company">Velmora Property Inspections, LLC</p>
        <p class="contact-address">4410 S. 58th St. Tempe, AZ 85283</p>
        <ul class="contact-lines">
          <li>
            <svg class="contact-icon" viewBox="0 0 16 16" aria-hidden="true">
              <path d="M3.2 1.5l2.4 2.6-1.3 1.8c.9 2 2.5 3.6 4.5 4.5l1.8-1.3 2.6 2.4-1.5 2.2C6.6 13.3 2.7 9.4 1 4.3z" fill="var(--green)"/>
            </svg>
            <span>+480-555-0172</span>
          </li>
          <li>
            <svg class="contact-icon" viewBox="0 0 16 16" aria-hidden="true">
              <rect x="1" y="3" width="14" height="10" fill="var(--green)"/>
              <path d="M1.5 3.5L8 9l6.5-5.5" fill="none" stroke="var(--card)" stroke-width="1.4"/>
            </svg>
            <span>glen@velmora-llc.example</span>
          </li>
        </ul>
      </div>
    </section>
  </main>
</body>
</html>
```